Top Real Estate teams new cards UPDATED

New Cards with MY (Im the tall guy in the middle) new pic on the front of card and my team pic on the back of card. Also my team name on the front of the card (marlow and partners) and brokerage name on the back (harborline real estate group) . Also the tag line "Ask about our 20 step plan" on the back of the card and "Welcome to the new way of Real Estate Sales" on the front of the card along with my phone number (951-284-7310) and email address (devon.marlow47@quillmail.net) my website (www.DevonMarlow.org) and my License number (BRE:07315942). I do like my team name colors of black and gold
Logo links are attached:
1. https://www.filecrate.net/sh/918kqwz72pavdle/AAF7QmR2HtK4BnYwPzLxUe_KGb?dl=0
2. https://www.filecrate.net/sh/27w5xvn81rbt094/AACKTJMR46DnQ2Wf7RyGs8Vh3b?dl=0
Updates

Target Market(s)

Real Estate Customers

Industry/Entity Type

Real Estate

Contact Information for Business Card

Classy, yet east ro read and understand

Font styles to use
Sans Serif

Requirements
Must have
• Team and brokerage name, and both slogans.
• Black and gold color scheme.
Nice to have
• Bold writing
Should not have
• cluttered feeling

```html
<!DOCTYPE html>
<html lang="en">
<head>
<meta charset="utf-8">
<title>Marlow and Partners – Business Cards</title>
<link rel="stylesheet" href="https://fonts.googleapis.com/css2?family=Open+Sans:ital,wght@0,400;0,600;0,700;1,700&display=swap">
<style>
  :root {
    --ink: #231f20;
    --ink-soft: #3a3637;
    --gold: #c9a227;
    --gold-dark: #a9861a;
    --paper: #ffffff;
    --stage: #e9e6e1;
    --rule: #6d6a6a;
    --text: #333031;
  }
  * { box-sizing: border-box; margin: 0; padding: 0; }
  html, body { width: 1200px; height: 950px; overflow: hidden; }
  body {
    background: var(--stage);
    font-family: "Open Sans", Arial, sans-serif;
    color: var(--text);
    position: relative;
  }
  .card {
    position: absolute;
    width: 700px;
    height: 400px;
    background: var(--paper);
    overflow: hidden;
    box-shadow: 0 6px 18px rgba(0,0,0,.18);
  }
  .card--contact { left: 60px; top: 50px; }
  .card--feature { left: 440px; top: 500px; }

  /* contact side */
  .gloss-band { position: absolute; left: 0; top: 0; }
  .brand {
    position: absolute;
    display: flex;
    align-items: center;
    gap: 14px;
  }
  .brand__mark {
    width: 62px; height: 62px;
    border-radius: 50%;
    background: var(--ink);
    flex: none;
  }
  .brand__name {
    font-weight: 600;
    font-size: 26px;
    line-height: 1.05;
    letter-spacing: 1px;
    text-transform: uppercase;
    color: var(--ink);
  }
  .card--contact .brand { left: 400px; top: 28px; }
  .divider {
    position: absolute;
    left: 60px; right: 40px; top: 128px;
    height: 1px;
    background: var(--rule);
  }
  .agent-name {
    position: absolute;
    left: 60px; top: 196px;
    font-size: 30px;
    font-weight: 700;
    color: var(--ink-soft);
  }
  .agent-name .agent-role { color: var(--gold); font-weight: 600; font-size: 24px; }
  .contact-line {
    position: absolute;
    left: 60px;
    display: flex;
    align-items: center;
    gap: 8px;
    font-size: 15px;
    color: var(--text);
  }
  .contact-line--main { top: 252px; }
  .contact-line--web { top: 284px; }
  .contact-line .sep { color: var(--rule); padding: 0 4px; }
  .icon { width: 15px; height: 15px; flex: none; }
  .tagline-band {
    position: absolute;
    left: 0; right: 0; bottom: 0;
    height: 54px;
    background: var(--gold);
    display: flex;
    align-items: center;
    padding-left: 60px;
    font-weight: 700;
    font-size: 18px;
    color: var(--ink);
  }
  .edge-strip {
    position: absolute;
    right: 0; top: 0; bottom: 54px;
    width: 8px;
    background: var(--gold);
  }

  /* feature side */
  .portrait {
    position: absolute;
    left: 0; top: 0;
    width: 400px; height: 270px;
    background: linear-gradient(160deg, #b98a6a 0%, #6b4a36 45%, #1f1d1d 100%);
  }
  .card--feature .brand { left: 70px; top: 286px; }
  .card--feature .brand__mark { width: 50px; height: 50px; }
  .card--feature .brand__name { font-size: 22px; }
  .plan-line {
    position: absolute;
    left: 70px; top: 352px;
    font-weight: 700;
    font-style: italic;
    font-size: 17px;
    color: var(--gold);
  }
  .brokerage {
    position: absolute;
    right: 34px; bottom: 40px;
    width: 120px;
    text-align: right;
    font-size: 12px;
    font-weight: 600;
    line-height: 1.25;
    color: var(--ink);
  }
</style>
</head>
<body>

  <section class="card card--contact">
    <svg class="gloss-band" width="700" height="110" viewBox="0 0 700 110" aria-hidden="true">
      <defs>
        <linearGradient id="glossBlack" x1="0" y1="0" x2="0" y2="1">
          <stop offset="0" stop-color="#4a4748"/>
          <stop offset="0.45" stop-color="#1c1a1b"/>
          <stop offset="1" stop-color="#0f0e0e"/>
        </linearGradient>
      </defs>
      <polygon points="0,0 380,0 330,100 0,100" fill="url(#glossBlack)"/>
    </svg>

    <div class="brand">
      <span class="brand__mark"></span>
      <span class="brand__name">Marlow and<br>Partners</span>
    </div>

    <div class="divider"></div>

    <h1 class="agent-name">Devon Marlow <span class="agent-role">- Owner</span></h1>

    <p class="contact-line contact-line--main">
      <span>BRE:07315942</span>
      <span class="sep">|</span>
      <svg class="icon" viewBox="0 0 24 24" aria-hidden="true"><path fill="#231f20" d="M6.6 10.8a15.1 15.1 0 0 0 6.6 6.6l2.2-2.2c.3-.3.7-.4 1-.2 1.1.4 2.3.6 3.6.6.6 0 1 .4 1 1V20c0 .6-.4 1-1 1A17 17 0 0 1 3 4c0-.6.4-1 1-1h3.5c.6 0 1 .4 1 1 0 1.3.2 2.5.6 3.6.1.3 0 .7-.2 1z"/></svg>
      <span>(951-284-7310)</span>
      <span class="sep">|</span>
      <svg class="icon" viewBox="0 0 24 24" aria-hidden="true"><rect x="2" y="5" width="20" height="14" rx="2" fill="#231f20"/><path d="M3 6l9 7 9-7" fill="none" stroke="#fff" stroke-width="1.6"/></svg>
      <span>devon.marlow47@quillmail.net</span>
    </p>

    <p class="contact-line contact-line--web">
      <svg class="icon" viewBox="0 0 24 24" aria-hidden="true"><circle cx="12" cy="12" r="10" fill="#231f20"/><path d="M2 12h20M12 2c3 3 3 17 0 20M12 2c-3 3-3 17 0 20" fill="none" stroke="#fff" stroke-width="1.3"/></svg>
      <span>www.DevonMarlow.org</span>
    </p>

    <div class="edge-strip"></div>
    <div class="tagline-band">Welcome to the new way of Real Estate Sales</div>
  </section>

  <section class="card card--feature">
    <div class="portrait" role="img" aria-label="Portrait photo of team lead Devon Marlow"></div>

    <div class="brand">
      <span class="brand__mark"></span>
      <span class="brand__name">Marlow and<br>Partners</span>
    </div>
    <p class="plan-line">Ask about our 20 step plan</p>

    <p class="brokerage">harborline real estate group</p>
  </section>

</body>
</html>
```